Business card needed for the Rydo of Dry Cleaning!

We need a slick business card design for a new company based out of Montreal called Casiers Plimo&Zet inc. (in French) and Plimo&Zet Lockers inc. (in English). We're the Rydo of Laundry. We offer services of dry cleaning, laundry (wash&fold), minor clothing alterations, shoe repair and parcel delivery through 24/7 secured and connected lockers. Ordres are placed through our mobile application. Real time notification are sent to customers when their order is ready for pickup. The lockers will be placed throughout the downtown area, in condo and office towers, where a high density of busy people converge. It is simple, user-friendly, and most importantly convenient. We're the out of the box dry cleaner, literally.

Target Market(s)

1) Professional workers wearing suits daily
2) Campus students living in residences
3) People using laundromats
4) Families with children/yuppies who prefer to use their time doing something else than laundry

Industry/Entity Type

Dry Cleaning

Contact Information for Business Card

Name / Annick-Solène Trudel
Title / CEO & Founder
Company Name / Casiers Plimo&Zet inc. | Plimo&Zet Lockers inc.
Website www.plimozet.ca

Requirements
Must have
• Text Logo: Plimo&Zet - Nettoyeurs 24/7 Cleaners
• Logo on one side and contact info on the other (bilingual)
• Minimalist, pure design
• "We care" for your belongings feeling
• Professional, technological, clean & fresh look
Should not have
• No busy visuals. No rainbow colors.

```html
<!DOCTYPE html>
<html lang="en">
<head>
<meta charset="utf-8">
<title>Plimo&amp;Zet Lockers – Business Card</title>
<link href="https://fonts.googleapis.com/css2?family=Montserrat:wght@600;700&family=Questrial&display=swap" rel="stylesheet">
<style>
  :root{
    --backdrop:#1c1c1e;
    --navy:#1b2547;
    --navy-deep:#141c38;
    --paper:#f5f5f5;
    --sky:#1a8fd6;
    --steel:#7f98b8;
    --white:#ffffff;
  }
  *{margin:0;padding:0;box-sizing:border-box}
  html,body{width:1200px;height:1001px;overflow:hidden;background:var(--backdrop)}
  .stage{position:relative;width:1200px;height:1001px}
  .card{position:absolute;left:306px;width:589px;height:330px;overflow:hidden;
        box-shadow:0 6px 14px rgba(0,0,0,.55)}
  .card--front{top:133px;background:var(--paper)}
  .card--back{top:540px;background:linear-gradient(180deg,var(--navy) 0%,var(--navy-deep) 100%)}
  .front-waves{position:absolute;inset:0;width:589px;height:330px}
  .brand{position:absolute;display:flex;align-items:center;gap:8px;
         font-family:"Montserrat",sans-serif;font-weight:700;letter-spacing:-.5px;line-height:1}
  .brand__mark{width:34px;height:34px;background:var(--sky);border-radius:4px;flex:none}
  .card--front .brand{left:44px;top:54px;font-size:40px;color:var(--navy)}
  .card--back .brand{left:50%;top:128px;transform:translateX(-50%);font-size:40px;color:var(--paper)}
  .person{position:absolute;left:45px;top:246px}
  .person__name{font-family:"Montserrat",sans-serif;font-weight:600;font-size:20px;
                color:var(--sky);letter-spacing:.3px;text-transform:uppercase}
  .person__title{font-family:"Questrial",sans-serif;font-size:16px;color:var(--white);margin-top:1px}
  .contact{position:absolute;left:356px;top:228px;list-style:none}
  .contact__item{display:flex;align-items:center;gap:12px;height:21.6px;
                 font-family:"Questrial",sans-serif;font-size:16px;color:var(--white)}
  .contact__icon{width:17px;height:17px;flex:none}
  .site-url{position:absolute;left:0;right:0;top:248px;text-align:center;
            font-family:"Questrial",sans-serif;font-size:16px;color:var(--white)}
  .site-url strong{font-family:"Montserrat",sans-serif;font-weight:700}
</style>
</head>
<body>
<main class="stage">

  <section class="card card--front" aria-label="Business card, contact side">
    <svg class="front-waves" viewBox="0 0 736 412" preserveAspectRatio="none" aria-hidden="true">
      <path fill="var(--navy)" d="M0,208 C120,250 230,266 330,226 C470,168 600,138 736,152 L736,412 L0,412 Z"/>
      <path fill="var(--paper)" d="M150,264 C300,254 420,178 560,140 C640,120 700,124 736,128 L736,152 C600,138 470,168 330,226 C260,254 200,262 150,264 Z"/>
      <path fill="var(--navy)" d="M145,262 C300,248 420,168 560,128 C640,108 700,112 736,120 L736,130 C690,122 630,122 560,142 C430,180 320,252 145,262 Z"/>
      <path fill="var(--sky)" d="M0,173 C80,210 190,226 275,210 C190,234 80,226 0,196 Z"/>
    </svg>

    <div class="brand"><span class="brand__mark"></span><span class="brand__name">Plimo&amp;Zet</span></div>

    <div class="person">
      <p class="person__name">Annick-Solène Trudel</p>
      <p class="person__title">CEO &amp; Founder</p>
    </div>

    <ul class="contact">
      <li class="contact__item">
        <svg class="contact__icon" viewBox="0 0 17 17" aria-hidden="true"><rect width="17" height="17" rx="3" fill="var(--sky)"/><path d="M5.5 3.5l2 2-1.2 1.4c.6 1.4 1.6 2.4 3 3l1.4-1.2 2 2-1.3 1.6c-3.6-.3-7-3.7-7.3-7.3z" fill="var(--white)"/></svg>
        <span>514-555-0187</span>
      </li>
      <li class="contact__item">
        <svg class="contact__icon" viewBox="0 0 17 17" aria-hidden="true"><rect width="17" height="17" rx="3" fill="var(--sky)"/><rect x="3.5" y="5" width="10" height="7" fill="none" stroke="var(--white)" stroke-width="1.1"/><path d="M3.5 5l5 4 5-4" fill="none" stroke="var(--white)" stroke-width="1.1"/></svg>
        <span>info@plimozet.ca</span>
      </li>
      <li class="contact__item">
        <svg class="contact__icon" viewBox="0 0 17 17" aria-hidden="true"><rect width="17" height="17" rx="3" fill="var(--sky)"/><g fill="none" stroke="var(--white)" stroke-width="1"><circle cx="8.5" cy="8.5" r="5"/><ellipse cx="8.5" cy="8.5" rx="2.2" ry="5"/><path d="M3.5 8.5h10M4.3 6h8.4M4.3 11h8.4"/></g></svg>
        <span>www.plimozet.ca</span>
      </li>
    </ul>
  </section>

  <section class="card card--back" aria-label="Business card, brand side">
    <div class="brand"><span class="brand__mark"></span><span class="brand__name">Plimo&amp;Zet</span></div>
    <p class="site-url">www.<strong>plimozet</strong>.ca</p>
  </section>

</main>
</body>
</html>
```